VELDAN Constructions stationery

Want following designed. Business cards. Letterhead. Email footer. A4 folder cover - front and side. Postcard. For two logo's. VELDAN CONSTRUCTIONS and VELDAN INTERIOR DESIGN. Logo's will be provided. Logo is black and metallic Gold.

We are a high end residential design and build company that builds for ourself and exclusive clients who we select to build for. We don't target high volume but high quality projects and build only for clients who pass a number of checks. Ultimately we choose our client and build very high end finishes in remodelling or new home builds. We have no website but will be designing one in the next month.

Target Market(s)

High end residential homes

Industry/Entity Type

Residential Construction

Font styles to use
Serif

Colors
000000
ffc214

Requirements
Must have
• Clean and simplistic. Must represent high end, sophistication, perfection and be sharp.
Nice to have
• We are a high end design and build company that is exclusive to clients we select to build for. We also add our own eclusive one off designs in each build for bathrooms and kitchens like towel rails, vanitys etc.
Should not have
• Animation or unsophisticated

```html
<!DOCTYPE html>
<html lang="en">
<head>
<meta charset="utf-8">
<title>VELDAN Interior Design – Business Card</title>
<link rel="stylesheet" href="https://fonts.googleapis.com/css2?family=Open+Sans:wght@400&family=Roboto:wght@400;500;700&display=swap">
<style>
  :root {
    --page-bg: #d9d3cb;
    --card-black: #050505;
    --card-black-soft: #2a2a2a;
    --gold-deep: #8a6a2c;
    --brand-tone: #e6dcc6;
    --frost-top: #f1efec;
    --frost-bottom: #ddd8d2;
    --ink: #2b2b2b;
    --ink-soft: #4a4a4a;
    --name-brown: #6e5a32;
    --tagline: #f2f2f2;
  }
  * { margin: 0; padding: 0; box-sizing: border-box; }
  html, body {
    width: 1200px; height: 969px; overflow: hidden;
    background: var(--page-bg);
  }
  .canvas { position: relative; width: 1200px; height: 969px; }
  .business-card {
    position: absolute; left: 100px; top: 200px;
    width: 1000px; height: 568px;
    border-radius: 4px; overflow: hidden;
    box-shadow: 0 18px 40px rgba(0,0,0,0.18);
    background: linear-gradient(180deg, var(--frost-top), var(--frost-bottom));
  }
  .brand-band {
    position: absolute; left: 0; top: 0; width: 100%; height: 305px;
    background: radial-gradient(ellipse at 50% 55%, var(--card-black-soft) 0%, var(--card-black) 70%);
    text-align: center;
  }
  .brand-band::after {
    content: ""; position: absolute; left: 0; bottom: 0; width: 100%; height: 3px;
    background: var(--gold-deep);
  }
  .brand-name {
    position: absolute; top: 118px; left: 0; width: 100%;
    font-family: "Open Sans", sans-serif; font-weight: 400;
    font-size: 42px; letter-spacing: 5px; line-height: 1;
    color: var(--brand-tone);
  }
  .brand-tagline {
    position: absolute; top: 240px; left: 0; width: 100%;
    font-family: "Open Sans", sans-serif; font-size: 21px;
    color: var(--tagline);
  }
  .brand-tagline .dot { color: var(--gold-deep); margin: 0 10px; }
  .person {
    position: absolute; left: 58px; top: 380px;
    font-family: "Roboto", sans-serif;
  }
  .person-name { font-size: 31px; font-weight: 500; color: var(--name-brown); line-height: 38px; }
  .person-title { font-size: 23px; font-weight: 700; color: var(--ink); line-height: 34px; }
  .person-address { font-size: 23px; color: var(--ink-soft); line-height: 33px; }
  .contact-list {
    position: absolute; right: 58px; top: 384px; list-style: none;
    font-family: "Roboto", sans-serif; font-size: 23px; color: var(--ink);
    text-align: right;
  }
  .contact-list li { line-height: 32px; display: flex; justify-content: flex-end; align-items: center; gap: 12px; }
  .contact-list svg { width: 22px; height: 22px; fill: var(--ink); }
</style>
</head>
<body>
<div class="canvas">
  <div class="business-card">
    <header class="brand-band">
      <p class="brand-name">VELDAN INTERIOR DESIGN</p>
      <p class="brand-tagline">Interior Architecture<span class="dot">·</span>Space design<span class="dot">·</span>Staging</p>
    </header>

    <section class="person">
      <p class="person-name">ADRIAN HOLT</p>
      <p class="person-title">CEO/FOUNDER</p>
      <p class="person-address">2140 Larkspur Way</p>
      <p class="person-address">Juneau, Alaska 99801</p>
    </section>

    <ul class="contact-list">
      <li>555 214 3090
        <svg viewBox="0 0 24 24" aria-hidden="true"><path d="M6.6 10.8a15.1 15.1 0 0 0 6.6 6.6l2.2-2.2c.3-.3.7-.4 1-.2 1.1.4 2.3.6 3.6.6.6 0 1 .4 1 1V20c0 .6-.4 1-1 1A17 17 0 0 1 3 4c0-.6.4-1 1-1h3.5c.6 0 1 .4 1 1 0 1.3.2 2.5.6 3.6.1.3 0 .7-.2 1z"/></svg>
      </li>
      <li>555 867 1142
        <svg viewBox="0 0 24 24" aria-hidden="true"><path d="M7 1h10a2 2 0 0 1 2 2v18a2 2 0 0 1-2 2H7a2 2 0 0 1-2-2V3a2 2 0 0 1 2-2zm0 3v14h10V4zm5 15.5a1.2 1.2 0 1 0 0 2.4 1.2 1.2 0 0 0 0-2.4z"/></svg>
      </li>
      <li>555 390 7726
        <svg viewBox="0 0 24 24" aria-hidden="true"><path d="M6 2h12v5H6zM3 8h18a2 2 0 0 1 2 2v7h-4v5H5v-5H1v-7a2 2 0 0 1 2-2zm4 8v4h10v-4zm11-5.5a1 1 0 1 0 0 2 1 1 0 0 0 0-2z"/></svg>
      </li>
      <li>studio@veldan.com
        <svg viewBox="0 0 24 24" aria-hidden="true"><path d="M2 5h20v14H2zm2 2v.5l8 5 8-5V7zm0 2.8V17h16V9.8l-8 5z"/></svg>
      </li>
    </ul>
  </div>
</div>
</body>
</html>
```